Local primary school needs a flyer design for their fundraising fete

I need a flyer design for a local primary school holding a fundraising fete. I would like to see designs that feature the school logo, school colours (red white and navy) and that reference/mention the main rides and stalls at the event. If possible I would like the sponsors (on the newsletter supplied) to be included and the photo of the school available on the website. The final design should be easy for me to print and produce myself so that can leave at local shops, cafes etc. leading up to the event.

School

Font styles to use
Serif

Colors
ec2027
ffffff

```html
<!DOCTYPE html>
<html lang="en">
<head>
<meta charset="utf-8">
<title>St Brigid's Primary School – Biannual Fete</title>
<link rel="stylesheet" href="https://fonts.googleapis.com/css2?family=Libre+Baskerville:ital,wght@0,400;0,700;1,400&family=Open+Sans:wght@600&display=swap">
<style>
  :root {
    --red: #ec2027;
    --white: #ffffff;
    --navy: #1d2a5b;
    --ink: #222222;
    --paper: #f2f2f2;
    --paper-shade: #e6e6e6;
    --backdrop: #8a8a8a;
    --photo-sky: #5d7fa6;
    --photo-wall: #b9b2a3;
  }
  * { box-sizing: border-box; margin: 0; padding: 0; }
  html, body { width: 1200px; height: 900px; overflow: hidden; }
  body {
    background: var(--backdrop);
    display: flex; align-items: center; justify-content: center;
    font-family: "Libre Baskerville", Georgia, serif;
    color: var(--ink);
  }
  .flyer {
    width: 600px; height: 850px;
    background: var(--paper);
    box-shadow: 0 6px 20px rgba(0,0,0,.25);
    display: flex; flex-direction: column;
  }
  .masthead { position: relative; }
  .masthead__strip { height: 12px; background: var(--red); }
  .masthead__photo {
    height: 108px;
    background: linear-gradient(100deg, var(--photo-sky) 0%, #8aa1bb 40%, var(--photo-wall) 70%, #8b6b4f 100%);
    position: relative;
  }
  .masthead__crest {
    position: absolute; left: 20px; top: 12px;
    width: 84px; height: 84px;
    background: var(--white);
    border: 3px solid var(--red);
    display: flex; align-items: center; justify-content: center;
    text-align: center;
    font-size: 11px; font-weight: 700; color: var(--red); line-height: 1.3;
  }
  .masthead__title {
    position: absolute; left: 124px; top: 34px;
    font-family: "Open Sans", Arial, sans-serif; font-weight: 600;
    color: var(--white); font-size: 24px; line-height: 1.1;
  }
  .masthead__title small { display: block; font-size: 14px; margin-top: 2px; }
  .intro { text-align: center; font-size: 15px; margin: 22px 0 10px; }
  .ribbon { display: block; margin: 0 auto; }
  .ribbon text { font-family: "Libre Baskerville", Georgia, serif; font-style: italic; }
  .date { text-align: center; margin-top: 2px; }
  .date__day { font-size: 20px; font-weight: 700; }
  .date__time { font-size: 16px; font-style: italic; }
  .details { padding: 10px 52px 18px; font-size: 12px; line-height: 1.45; text-align: justify; }
  .sponsors { background: var(--paper-shade); flex: 1; padding: 16px 40px 20px; }
  .sponsors__heading { color: var(--red); text-align: center; font-size: 14px; font-weight: 700; letter-spacing: .5px; text-transform: uppercase; }
  .sponsors__thanks { font-size: 11px; text-align: center; margin: 6px 0 16px; line-height: 1.4; }
  .sponsor-grid {
    list-style: none;
    display: grid; grid-template-columns: repeat(4, 1fr);
    gap: 14px 12px; align-items: center;
  }
  .sponsor {
    display: flex; align-items: center; gap: 6px;
    font-size: 13px; font-weight: 700; color: var(--navy); line-height: 1.15;
  }
  .sponsor::before {
    content: ""; flex: 0 0 10px; height: 10px; background: var(--red);
  }
</style>
</head>
<body>
  <article class="flyer">
    <header class="masthead">
      <div class="masthead__strip"></div>
      <div class="masthead__photo" role="img" aria-label="Photograph of the school building entrance">
        <div class="masthead__crest">St Brigid's<br>Larchmont</div>
        <h1 class="masthead__title">St Brigid's Primary School<small>Larchmont, Canberra</small></h1>
      </div>
      <div class="masthead__strip"></div>
    </header>

    <p class="intro">St Brigid's Primary School in Larchmont will hold their</p>

    <svg class="ribbon" width="300" height="62" viewBox="0 0 300 62" aria-hidden="false">
      <polygon points="0,18 40,18 40,52 0,52 14,35" fill="#b3161c"/>
      <polygon points="300,18 260,18 260,52 300,52 286,35" fill="#b3161c"/>
      <path d="M28,8 Q150,-4 272,8 L272,44 Q150,32 28,44 Z" fill="var(--red)"/>
      <text x="150" y="32" text-anchor="middle" font-size="22" fill="#ffffff">biannual fete</text>
    </svg>

    <div class="date">
      <div class="date__day">Sunday 21 September</div>
      <div class="date__time">from 11.00am to 3.00pm</div>
    </div>

    <p class="details">There will be some fantastic rides, including jumping castles, horizontal bungy and if you're game, even a wild bucking bull! There will also be the old fete favourites, including the petting zoo, arts and craft, the chocolate wheel and the cake stall to name a few along with other wonderful treats and delicious food to eat. With over 20 stalls, there will be something for everyone. So come along for a family excursion filled with fun and some bargain buys too.</p>

    <section class="sponsors">
      <h2 class="sponsors__heading">2014 St Brigid's Fete Gold &amp; Silver Sponsors</h2>
      <p class="sponsors__thanks">Thank you to our generous sponsors. Please take note of the advertisements below<br>and support these wonderful businesses where you can.</p>
      <ul class="sponsor-grid">
        <li class="sponsor">Kestrel Plumbing</li>
        <li class="sponsor">Harbour Line Realty</li>
        <li class="sponsor">Bytefold</li>
        <li class="sponsor">The Linen Room</li>
        <li class="sponsor">Ridgeway Motors</li>
        <li class="sponsor">Velvet Lane</li>
        <li class="sponsor">Timberstep Decks</li>
        <li class="sponsor">Corvale Group</li>
        <li class="sponsor">Luma Hair</li>
        <li class="sponsor">Aegean Club</li>
        <li class="sponsor">Stride Sports</li>
        <li class="sponsor">Brightwater Dental</li>
        <li class="sponsor">Numera</li>
        <li class="sponsor">Wayfare Travel</li>
        <li class="sponsor">Quarry Theatre</li>
        <li class="sponsor">Alignwell Osteopathy</li>
        <li class="sponsor">Gift Hamper Co.</li>
      </ul>
    </section>
  </article>
</body>
</html>
```